Geschäftspapiere für Software für die Logistikbranche
Zielgruppe
Wir haben eine Software für die Logistikbranche entwickelt. Nutzen dieser Software ist die Digitalisierung von Geschäftsprozessen, eine digitale Tourenvergabe und die Reduktion der Frachtkosten im Unternehmen.
Zielgruppe: B2B, verladendes Gewerbe, jeder der etwas versenden muss
Aufgabenstellung
Die Farbe Orange sollte verwendet werden. Der Briefkopf soll in erster Linie für die Kundenakquise genutzt werden. In zweiter Linie für normale Kommunikation. Die Vorlage sollte etwas für das Auge sein, damit der Text gut zur Geltung kommt. Ein Störer wäre ideal, um Sonderaktionen oder Rabatte in das Anschreiben mit einzubauen.
In der Fußzeile sollten Platzhalter für alle unternehmensbezogenen Daten sein.

```html
<!DOCTYPE html>
<html lang="de">
<head>
<meta charset="utf-8">
<title>Briefbogen – Ladewerk Logistik</title>
<link rel="stylesheet" href="https://fonts.googleapis.com/css2?family=Inter:wght@400;600;700&display=swap">
<style>
  :root {
    --orange: #fb8a0a;
    --slate: #58595e;
    --paper: #ffffff;
    --frame: #e6e6e6;
  }
  * { margin: 0; padding: 0; box-sizing: border-box; }
  html, body {
    width: 846px;
    height: 1200px;
    overflow: hidden;
    background: var(--paper);
  }
  .letterhead {
    position: relative;
    width: 846px;
    height: 1200px;
    background: var(--paper);
    border: 1px solid var(--frame);
    font-family: "Inter", Arial, sans-serif;
    color: var(--slate);
    overflow: hidden;
  }
  .top-band {
    position: absolute;
    top: 0;
    right: 0;
    width: 250px;
    height: 43px;
    background: var(--orange);
    border-bottom-left-radius: 22px;
  }
  .brand-name {
    position: absolute;
    top: 168px;
    right: 19px;
    font-size: 22px;
    font-weight: 600;
    letter-spacing: 0.5px;
    color: var(--orange);
  }
  .sender {
    position: absolute;
    top: 230px;
    right: 19px;
    text-align: right;
    font-size: 18px;
    line-height: 24px;
    font-weight: 400;
  }
  .sender-company {
    font-size: 19px;
    font-weight: 700;
    line-height: 26px;
  }
  .footer-band {
    position: absolute;
    left: 0;
    bottom: 0;
    width: 499px;
    height: 83px;
    background: var(--slate);
    border-top-right-radius: 39px;
    display: flex;
    align-items: center;
    justify-content: center;
    padding-bottom: 6px;
  }
  .website {
    color: var(--paper);
    font-size: 25px;
    font-weight: 400;
  }
</style>
</head>
<body>
  <div class="letterhead">
    <div class="top-band"></div>

    <div class="brand-name">LADEWERK</div>

    <address class="sender" style="font-style: normal;">
      <div class="sender-company">LADEWERK LOGISTIK</div>
      <div>Hafenweg 27</div>
      <div>45127 Beispielstadt</div>
      <div>Telefon: 0201 55501842</div>
      <div>E-Mail: info@yourmail.de</div>
    </address>

    <footer class="footer-band">
      <span class="website">www.yoursite.com</span>
    </footer>
  </div>
</body>
</html>
```